A Weather Forecasting Site needs designs

We need a website design for our new venture which is a weather forecasting website. This website should have the latest design trends.

Menu
Weather, Maps, Videos and Photos

The home page requirements are as follows:
- Search Bar
- Local Weather
- Weather forecast of major cities in the World
Favorite locations
- Space for ADs
- Email signup

Weather Details page
This page will be redirected from the home page when you click on any of the weather forecast section

We are open to all kinds of designs and ideas. Feel free to you colors which suite your design.

```html
<!DOCTYPE html>
<html lang="en">
<head>
<meta charset="utf-8">
<title>Skycast – Weather Forecast</title>
<link href="https://fonts.googleapis.com/css2?family=Montserrat:wght@400;500;600;700;800&family=Roboto:wght@400;500&family=Oswald:wght@400;500&display=swap" rel="stylesheet">
<style>
:root{
  --ink:#111111;
  --bar:#0b0b0b;
  --orange:#f7931e;
  --orange-deep:#ef7d12;
  --text:#222222;
  --muted:#555555;
  --soft:#f2f2f2;
  --line:#cfcfcf;
  --footer:#1b1b1b;
  --footer-base:#0a0a0a;
  --white:#ffffff;
  --blue:#1b75bb;
}
*{box-sizing:border-box;margin:0;padding:0}
html,body{width:1200px;height:2347px;overflow:hidden}
body{position:relative;background:var(--white);font-family:"Montserrat",sans-serif;color:var(--text)}
.abs{position:absolute}
a{color:inherit;text-decoration:none}

/* top strip */
.topbar{left:0;top:0;width:1200px;height:25px;background:var(--bar);color:#ddd;font-size:10px;display:flex;align-items:center}
.topbar .lang{position:absolute;left:56px;display:flex;align-items:center;gap:6px}
.topbar .crumbs{position:absolute;left:197px;display:flex;align-items:center;gap:9px}
.topbar .flag{width:14px;height:9px;background:linear-gradient(#b22 0 50%,#eee 50%);border-left:6px solid #2a3f8f}
.topbar .user{position:absolute;left:488px;display:flex;align-items:center;gap:6px}
.topbar .search{position:absolute;left:945px;top:0;width:165px;height:25px;background:var(--white);color:#888;font-size:9px;padding:7px 0 0 13px}
.topbar .search-btn{position:absolute;left:1110px;top:0;width:34px;height:25px;background:var(--orange);display:flex;align-items:center;justify-content:center}

/* header */
.brand{left:55px;top:58px;display:flex;align-items:center;gap:12px}
.brand .mark{width:18px;height:18px;border-radius:50%;background:var(--orange)}
.brand .name{font-weight:700;font-size:40px;letter-spacing:.5px;color:#2b2b2b;line-height:1}
.promo{left:500px;top:41px;width:644px;height:86px;background:linear-gradient(90deg,#3a3a3a,#2c2c2c 40%,#3b2a26);overflow:hidden}
.promo .shot{position:absolute;left:0;top:0;width:140px;height:86px;background:linear-gradient(135deg,#d9d9d9,#8e8e8e)}
.promo .l1{position:absolute;left:157px;top:10px;font-weight:800;font-size:23px;color:var(--white)}
.promo .tag{position:absolute;left:283px;top:12px;font-size:9px;color:#ddd;line-height:1.2}
.promo .tag b{color:var(--orange);font-weight:600}
.promo .l2{position:absolute;left:157px;top:42px;font-weight:800;font-size:23px;color:var(--orange)}
.promo .l2 span{font-weight:500;font-size:17px;color:var(--white)}
.promo .buy{position:absolute;left:508px;top:24px;width:116px;height:32px;background:var(--orange);color:var(--white);font-size:11px;font-weight:700;display:flex;align-items:center;justify-content:center}

/* main nav */
.mainnav{left:0;top:141px;width:1200px;height:40px;background:var(--bar);color:var(--white);font-size:13px}
.mainnav .now{position:absolute;left:55px;top:0;width:149px;height:40px;background:#3a3a3a;display:flex;align-items:center;justify-content:center;color:#ddd}
.mainnav .item{position:absolute;top:0;height:40px;display:flex;align-items:center;justify-content:center;border-right:1px solid #444}
.mainnav .watch{position:absolute;left:970px;top:0;width:174px;height:40px;background:var(--orange);display:flex;align-items:center;justify-content:center;gap:10px;font-size:14px;font-weight:500}

/* sub strip */
.substrip{left:0;top:183px;width:1200px;height:67px;background:var(--soft);font-size:14px;font-weight:500;color:#333}
.substrip .ico{position:absolute;top:6px;width:55px;height:55px;border-radius:50%;background:var(--white);display:flex;align-items:center;justify-content:center}
.substrip .lbl{position:absolute;top:24px}

/* hero */
.hero{left:55px;top:252px;width:709px;height:368px;background:linear-gradient(180deg,#4a5a4a 0%,#2c3a30 45%,#1d261f 100%)}
.now-card{left:30px;top:74px;width:150px;height:88px;background:var(--white);padding:4px 7px;font-size:12px;color:#222;white-space:nowrap}
.now-card small{display:block;font-size:8px;color:#444;line-height:1.3}
.now-card .temp{display:flex;align-items:center;gap:8px;margin-top:3px;font-size:32px;line-height:1}
.now-card .temp sup{font-size:10px;align-self:flex-start;margin-top:2px}
.now-card .sun{width:24px;height:24px;border-radius:50%;background:#f6b81a;flex:none}
.chip{top:139px;height:19px;background:var(--orange);color:var(--white);font-size:8px;font-weight:700;display:flex;align-items:center;justify-content:center;gap:6px;border:1px solid #ffb35b}
.chip span{font-weight:400;font-size:7px}

/* sidebar */
.follow{left:807px;top:278px;font-size:20px;color:#222}
.follow-rule{left:807px;top:324px;width:338px;height:3px;background:#222}
.follow-rule::after{content:"";position:absolute;left:22px;top:3px;border:6px solid transparent;border-top-color:#222}
.socials{left:807px;top:347px;display:flex;gap:6px}
.socials i{display:block;width:33px;height:33px}
.mapcta{left:807px;top:407px;width:338px;height:219px;background:linear-gradient(135deg,#3f8fb0,#6f9e6a 45%,#b9a266 70%,#4a93b8);display:flex;align-items:center;justify-content:center;text-align:center;color:var(--white);font-weight:700;font-size:23px;line-height:1.45}

/* cards */
.card{top:657px;width:327px;height:286px}
.card .head{height:47px;background:var(--ink);color:var(--white);font-size:21px;font-weight:500;padding:10px 0 0 37px;white-space:nowrap}
.card .media{position:absolute;top:47px;left:0;width:100%;height:239px}
.card .caption{position:absolute;left:0;bottom:0;width:100%;height:45px;background:rgba(255,255,255,.75);font-size:16px;color:#333;padding:12px 0 0 70px}
.card .badge{position:absolute;left:0;bottom:0;width:50px;height:45px;background:var(--orange);display:flex;align-items:center;justify-content:center;z-index:1}

/* data portal */
.portal{left:805px;top:665px;width:341px;height:383px;border:2px solid #555;padding:0 16px}
.portal h3{margin-top:28px;font-size:27px;font-weight:500;color:var(--blue);font-family:"Roboto",sans-serif}
.portal hr{border:0;border-top:1px solid #bbb;margin:6px 0 10px}
.portal h4{font-family:"Roboto",sans-serif;font-weight:400;font-size:25px;color:#222}
.portal p{font-family:"Roboto",sans-serif;font-size:15px;line-height:1.3;margin-top:8px;color:#222;width:262px}
.portal .more{position:absolute;left:242px;top:182px;color:var(--orange-deep);font-size:14px;font-family:"Roboto",sans-serif}
.portal .sat{position:absolute;left:16px;top:240px;width:303px;height:122px;background:radial-gradient(circle at 65% 50%,#e9eef2 0 10%,#8aa0b4 22%,#2b4f7c 60%,#1c3556)}

/* big map */
.bigmap{left:55px;top:983px;width:709px;height:414px}
.bigmap .head{height:45px;background:var(--ink);color:var(--white);font-size:21px;font-weight:500;padding:10px 0 0 39px}
.bigmap .media{position:absolute;top:45px;left:0;width:709px;height:369px;background:linear-gradient(160deg,#2c5a8c 0%,#5c7a3e 30%,#8b7b52 55%,#4c7a3a 75%,#2a5a96 100%)}

/* advertise */
.advert{left:807px;top:1091px;width:338px;height:306px;background:linear-gradient(#2a2a2a,#111)}
.advert .panel{position:absolute;left:50px;top:27px;width:226px;height:254px;background:rgba(120,120,120,.55);text-align:center;color:var(--white)}
.advert .s1{margin-top:54px;font-family:"Oswald",sans-serif;font-size:16px;line-height:1.15;color:#eee}
.advert .s2{font-family:"Oswald",sans-serif;font-weight:500;font-size:38px;line-height:1.05;margin-top:6px}
.advert .s3{font-family:"Oswald",sans-serif;font-weight:500;font-size:38px;line-height:1;color:var(--orange)}
.advert .stars{display:flex;justify-content:center;gap:6px;margin-top:8px}

/* conditions */
.cond-title{left:0;top:1437px;width:1200px;text-align:center;font-size:28px;font-weight:600;color:#111}
.cond{left:53px;top:1503px;width:1093px;height:407px;border:2px solid #d0d0d0;display:grid;grid-template-columns:1fr 1fr;grid-template-rows:repeat(5,1fr);background:#f3f3f3}
.cond .cell{position:relative;border-bottom:2px solid #d0d0d0;font-family:"Roboto",sans-serif}
.cond .cell:nth-child(odd){border-right:2px solid #d0d0d0}
.cond .cell:nth-last-child(-n+2){border-bottom:0}
.cond .place{position:absolute;left:27px;top:25px;font-size:24px;color:#333}
.cond .wx{position:absolute;left:355px;top:14px}
.cond .deg{position:absolute;left:455px;top:30px;font-size:21px;color:#222}

/* footer */
.footer{left:0;top:1959px;width:1200px;height:310px;background:var(--footer);color:var(--white)}
.footer .col{position:absolute;top:37px}
.footer h5{font-size:19px;font-weight:500;margin-bottom:22px;letter-spacing:.2px}
.footer ul{list-style:none;font-size:14px;line-height:31px;color:#eee}
.footer-base{left:0;top:2269px;width:1200px;height:78px;background:var(--footer-base);color:#ddd;font-size:14px}
.footer-base .copy{position:absolute;left:58px;top:29px}
.footer-base .social{position:absolute;left:1010px;top:28px;display:flex;gap:9px}
.footer-base .social i{display:block;width:17px;height:17px;border-radius:50%}
</style>
</head>
<body>

<header>
  <div class="abs topbar">
    <div class="lang">
      <svg width="11" height="11" viewBox="0 0 12 12"><circle cx="6" cy="6" r="5" fill="none" stroke="#ddd"/><path d="M1 6h10M6 1c-3 3-3 7 0 10M6 1c3 3 3 7 0 10" fill="none" stroke="#ddd" stroke-width=".8"/></svg>
      <span>ENGLISH (US), °C</span>
    </div>
    <div class="crumbs">
      <i class="flag"></i><span>▾</span><span>World</span><span>›</span><span>America</span><span>›</span><span>Lorem</span><span>›</span><span>Epsam</span>
    </div>
    <div class="user">
      <svg width="10" height="11" viewBox="0 0 10 11"><circle cx="5" cy="3" r="2.6" fill="#ddd"/><path d="M0 11c0-4 10-4 10 0z" fill="#ddd"/></svg>
      <span>Singup</span>
    </div>
    <div class="search">Search...</div>
    <div class="search-btn"><svg width="14" height="14" viewBox="0 0 14 14"><circle cx="6" cy="6" r="4.3" fill="none" stroke="#fff" stroke-width="2"/><path d="M9.2 9.2L13 13" stroke="#fff" stroke-width="2.2"/></svg></div>
  </div>

  <div class="abs brand"><i class="mark"></i><span class="name">Skycast</span></div>

  <div class="abs promo">
    <div class="shot" role="img" aria-label="Screenshots of the magazine theme"></div>
    <div class="l1">ASK THE</div>
    <div class="tag">An Amazingly Fresh <b>News/Magazine</b> Theme<br>for SitePress</div>
    <div class="l2">USERS ABOUT BREEZE <span>News?</span></div>
    <div class="buy">BUY NOW</div>
  </div>

  <nav class="abs mainnav">
    <div class="now">Now 1:07 pm IST</div>
    <div class="item" style="left:204px;width:157px">Weekend</div>
    <div class="item" style="left:361px;width:133px">Extended</div>
    <div class="item" style="left:494px;width:117px">Month</div>
    <div class="item" style="left:611px;width:115px">Satellite</div>
    <div class="watch">Watch Videos <svg width="13" height="13" viewBox="0 0 14 14"><circle cx="7" cy="7" r="6" fill="none" stroke="#fff"/><path d="M5.5 4.5l4 2.5-4 2.5z" fill="#fff"/></svg></div>
  </nav>

  <div class="abs substrip">
    <div class="ico" style="left:80px"><svg width="32" height="26" viewBox="0 0 32 26"><path d="M8 20a6 6 0 0 1 1-12 8 8 0 0 1 15 2 5 5 0 0 1 0 10z" fill="none" stroke="#333" stroke-width="1.6"/><path d="M12 22l-1 3M17 22l-1 3M22 22l-1 3" stroke="#333" stroke-width="1.4"/></svg></div>
    <div class="lbl" style="left:160px">America Weather</div>
    <div class="ico" style="left:331px"><svg width="32" height="28" viewBox="0 0 32 28"><circle cx="13" cy="11" r="6" fill="#f6b81a"/><path d="M10 24a5 5 0 0 1 1-10 7 7 0 0 1 13 2 4 4 0 0 1 0 8z" fill="#cfd6dc"/><path d="M14 25l-1 2M19 25l-1 2" stroke="#6aa9d8" stroke-width="1.4"/></svg></div>
    <div class="lbl" style="left:426px">New York , America &nbsp;&nbsp;Local Weather36˚C</div>
    <div class="ico" style="left:768px"><svg width="22" height="22" viewBox="0 0 22 22" stroke="#3d8fd6" stroke-width="1.6"><path d="M11 1v20M2 6l18 10M2 16l18-10"/></svg></div>
    <div class="lbl" style="left:855px">Personalized Forecasts: &nbsp;&nbsp;&nbsp;Allergies</div>
  </div>
</header>

<main>
  <section class="abs hero" role="img" aria-label="Photo of a misty forest with a hooded figure among tall trees">
    <div class="abs now-card">
      Washington, DC, USA
      <small>Monday 7:00 AM<br>Sunny</small>
      <div class="temp"><i class="sun"></i>12<sup>°C|°F</sup></div>
    </div>
    <div class="abs chip" style="left:225px;width:99px">CURRENT WEATHER</div>
    <div class="abs chip" style="left:348px;width:99px">TODAY <span>May 15</span></div>
    <div class="abs chip" style="left:467px;width:99px">TONIGHT <span>May 15</span></div>
    <div class="abs chip" style="left:589px;width:99px">TOMORROW <span>May 16</span></div>
  </section>

  <aside>
    <div class="abs follow">Follow us</div>
    <div class="abs follow-rule"></div>
    <div class="abs socials">
      <i style="background:#f7931e"></i><i style="background:#3b7fc4"></i><i style="background:#e0302b"></i><i style="background:#5aa7dd"></i><i style="background:#3b5998"></i><i style="background:#2aa5e0"></i>
    </div>
    <div class="abs mapcta" role="img" aria-label="World map background">VIEW STELIGHT<br>MAP</div>

    <div class="abs portal">
      <h3>Weather Data Portal</h3>
      <hr>
      <h4>ClimaPoint in XML</h4>
      <p>ClimaPoint Global is the simplest way to get ClimaPoint's Weather Data at your end, starting at US$ 0.69/month</p>
      <span class="more">more&gt;</span>
      <div class="sat" role="img" aria-label="Satellite image of a hurricane over the sea"></div>
    </div>

    <div class="abs advert" role="img" aria-label="Advertising banner with raised hands in the background">
      <div class="panel">
        <div class="s1">Best Solution<br>for Your Business</div>
        <div class="s2">ADVERTISE</div>
        <div class="s3">HERE</div>
        <div class="stars">
          <svg width="100" height="16" viewBox="0 0 100 16"><defs><path id="st" d="M8 0l2.4 5 5.6.8-4 3.9.9 5.5L8 12.6 3.1 15.2 4 9.7 0 5.8 5.6 5z"/></defs><use href="#st" fill="#f7b21e"/><use href="#st" x="21" fill="#f7b21e"/><use href="#st" x="42" fill="#f7b21e"/><use href="#st" x="63" fill="#fff"/><use href="#st" x="84" fill="#fff"/></svg>
        </div>
      </div>
    </div>
  </aside>

  <article class="abs card" style="left:55px">
    <div class="head">Video Weather Forecast</div>
    <div class="media" role="img" aria-label="Presenter standing before a weather map" style="background:linear-gradient(120deg,#22325a 0%,#3f6ea8 35%,#8fb1d6 70%,#c9d7e6)">
      <div class="badge"><svg width="24" height="22" viewBox="0 0 24 22"><circle cx="9" cy="8" r="4.5" fill="none" stroke="#fff" stroke-width="1.6"/><path d="M7 20a4 4 0 0 1 1-8 6 6 0 0 1 11 2 3 3 0 0 1 0 6z" fill="#fff"/></svg></div>
      <div class="caption">America Weather</div>
    </div>
  </article>

  <article class="abs card" style="left:438px">
    <div class="head" style="padding-left:25px">America Weather Satellite</div>
    <div class="media" role="img" aria-label="Satellite weather map of the world" style="background:linear-gradient(160deg,#244f8c,#4a7bb5 40%,#b58f5a 60%,#3a6aa6)">
      <div class="caption" style="padding-left:21px">See Weather Satellite</div>
    </div>
  </article>

  <section class="abs bigmap">
    <div class="head">America Weather Map - Nearby Places</div>
    <div class="media" role="img" aria-label="Weather map of North America with city forecasts for Seattle, Denver, Chicago, New York, Atlanta, Dallas and Miami"></div>
  </section>

  <h2 class="abs cond-title">America Weather Conditions - Nearby Places division</h2>
  <section class="abs cond">
    <svg width="0" height="0" style="position:absolute"><defs><g id="wx"><g stroke="#f7931e" stroke-width="1.6" fill="none"><circle cx="20" cy="20" r="7.5"/><path d="M20 4v5M20 31v5M4 20h5M8.7 8.7l3.5 3.5M31.3 8.7l-3.5 3.5M8.7 31.3l3.5-3.5"/></g><path d="M18 44a7 7 0 0 1 1-14 9.5 9.5 0 0 1 17.5 3 5.5 5.5 0 0 1 0 11z" fill="#f3f3f3" stroke="#999" stroke-width="1.5"/></g></defs></svg>
    <div class="cell"><span class="place">Haora</span><svg class="wx" width="50" height="48"><use href="#wx"/></svg><span class="deg">33°</span></div>
    <div class="cell"><span class="place">Atghara</span><svg class="wx" width="50" height="48"><use href="#wx"/></svg><span class="deg">33°</span></div>
    <div class="cell"><span class="place">Chak Kolarkhal</span><svg class="wx" width="50" height="48"><use href="#wx"/></svg><span class="deg">33°</span></div>
    <div class="cell"><span class="place">Mukundapur</span><svg class="wx" width="50" height="48"><use href="#wx"/></svg><span class="deg">33°</span></div>
    <div class="cell"><span class="place">Karimpur</span><svg class="wx" width="50" height="48"><use href="#wx"/></svg><span class="deg">33°</span></div>
    <div class="cell"><span class="place">Haridevpur</span><svg class="wx" width="50" height="48"><use href="#wx"/></svg><span class="deg">33°</span></div>
    <div class="cell"><span class="place">Bhagabanpur</span><svg class="wx" width="50" height="48"><use href="#wx"/></svg><span class="deg">33°</span></div>
    <div class="cell"><span class="place">Krishnanagar</span><svg class="wx" width="50" height="48"><use href="#wx"/></svg><span class="deg">33°</span></div>
    <div class="cell"><span class="place">Jagatipata</span><svg class="wx" width="50" height="48"><use href="#wx"/></svg><span class="deg">33°</span></div>
    <div class="cell"><span class="place">Ramkantapur</span><svg class="wx" width="50" height="48"><use href="#wx"/></svg><span class="deg">33°</span></div>
  </section>
</main>

<footer>
  <div class="abs footer">
    <div class="col" style="left:56px">
      <h5>COMPANY</h5>
      <ul><li>Precision in Every Forecast</li><li>About Skycast</li><li>Media Kit</li><li>Careers</li><li>Press</li><li>Contact Us</li></ul>
    </div>
    <div class="col" style="left:490px">
      <h5>PRODUCTS &amp; SERVICES</h5>
      <ul style="line-height:27.5px"><li>Enterprise Solutions</li><li>Q3 Data Analytics</li><li>Forecast Network</li><li>NarrateDesk</li><li>Tools for Broadcast</li><li>Radio &amp; Newspaper</li><li>Weather APIs</li></ul>
    </div>
    <div class="col" style="left:918px">
      <h5>APPS &amp; DOWNLOADS</h5>
      <ul><li>Phone App</li><li>Tablet App</li><li>Desktop App</li><li>See all Apps &amp; Downloads</li></ul>
    </div>
  </div>
  <div class="abs footer-base">
    <div class="copy">© 2017 Skycast, Inc. All Rights Reserved.</div>
    <div class="social"><i style="background:#3b5998"></i><i style="background:#2aa5e0"></i><i style="background:#dd4b39"></i><i style="background:#0e76a8"></i><i style="background:#cb2027"></i></div>
  </div>
</footer>

</body>
</html>
```